Ridgeway Truck & Bus Center, Truck Repair, Light.medium duty trucks

May an eye catching banner for Truck & Bus Repair to be used on Facebook, Possibly printable banner.

Target Market(s)

Need to target Fleet's or walk in customers for Light, Medium and Heavy Duty Truck and Bus Repairs

Industry/Entity Type

Truck Repair

Other font styles liked:
• Please see my sample uploaded

Requirements
Must have
• Some visually appealing, Use of logo, a modern look and feel to design. Would like market towards medium duty and heavy duty truck repair clientele.
Nice to have
• If can get logos of vehicle makes which can be seen in my sample I uploaded. Please add kelbro mfg logo as I’m a warranty ac repair facility, as well as please refer to all other make logos in my sample
Uploaded would I.e. varn, Dastorene, Pelloway,Brin,voltan etc please see sample for all other logo makes.

```html
<!DOCTYPE html>
<html lang="en">
<head>
<meta charset="utf-8">
<title>Ridgeway Truck &amp; Bus Center – Repair Banner</title>
<link rel="stylesheet" href="https://fonts.googleapis.com/css2?family=Roboto+Condensed:wght@300;400;700;800&family=Open+Sans:wght@600&family=Montserrat:wght@500&display=swap">
<style>
  :root {
    --page-bg: #d9d9d9;
    --red-deep: #6e0010;
    --red: #9b0018;
    --red-bright: #b0101f;
    --ink: #121212;
    --white: #ffffff;
    --muted: #bdbdbd;
  }
  * { margin: 0; padding: 0; box-sizing: border-box; }
  html, body { width: 1200px; height: 537px; overflow: hidden; background: var(--page-bg); }

  .banner {
    position: absolute; left: 20px; top: 55px;
    width: 1160px; height: 427px;
    overflow: hidden;
    box-shadow: 3px 4px 6px rgba(0,0,0,.35);
    color: var(--white);
  }
  .banner-art { position: absolute; inset: 0; width: 100%; height: 100%; }

  .kicker {
    position: absolute; left: 490px; top: 48px;
    font: 400 22px/1 "Roboto Condensed", sans-serif;
    letter-spacing: .1px;
  }
  .headline {
    position: absolute; left: 488px; top: 76px;
    font: 800 50px/1 "Roboto Condensed", sans-serif;
    letter-spacing: -.2px;
  }
  .tagline {
    position: absolute; left: 490px; top: 127px; width: 542px; height: 29px;
    background: var(--ink);
    clip-path: polygon(1.2% 0, 100% 0, 98.8% 100%, 0 100%);
    font: 300 16.5px/29px "Roboto Condensed", sans-serif;
    padding-left: 17px;
  }

  .services {
    position: absolute; top: 179px; left: 493px;
    display: grid; grid-template-columns: 238px auto; row-gap: 5px;
    list-style: none;
    font: 600 21.5px/23px "Open Sans", sans-serif;
  }
  .services li { position: relative; padding-left: 13px; }
  .services li::before {
    content: ""; position: absolute; left: 0; top: 3px;
    width: 6px; height: 6px; border-radius: 50%; background: var(--ink);
  }

  .contact {
    position: absolute; left: 501px;
    display: flex; align-items: center; gap: 6px;
    font: 500 19px/1 "Montserrat", sans-serif;
  }
  .contact-phones { top: 298px; gap: 0; }
  .phone { display: flex; align-items: center; gap: 6px; margin-right: 16px; }
  .contact-address { top: 326px; }
  .icon { width: 15px; height: 15px; flex: none; }

  .brand-strip {
    position: absolute; left: 18px; top: 373px; height: 54px; width: 890px;
    display: flex; align-items: center; justify-content: space-between;
    list-style: none;
    font: 700 11px/1 "Roboto Condensed", sans-serif;
    color: var(--white);
    text-transform: uppercase; letter-spacing: .3px;
  }
  .brand-strip .group-gap { width: 12px; }

  .client-mark {
    position: absolute; left: 937px; top: 340px; width: 212px;
    text-align: center; color: var(--white);
    font-family: "Roboto Condensed", sans-serif; font-weight: 800;
  }
  .client-name { font-size: 35px; line-height: 1; letter-spacing: .5px; }
  .client-sub { font-size: 9px; letter-spacing: 3px; margin-top: 4px; }
</style>
</head>
<body>
<section class="banner" aria-label="Ridgeway Truck and Bus Center repair banner">
  <svg class="banner-art" viewBox="0 0 2075 763" preserveAspectRatio="none" aria-hidden="false">
    <defs>
      <linearGradient id="redField" x1="0" y1="0" x2="1" y2="0.3">
        <stop offset="0" stop-color="#b0101f"/>
        <stop offset=".55" stop-color="#920016"/>
        <stop offset="1" stop-color="#5e000c"/>
      </linearGradient>
      <linearGradient id="workshopPhoto" x1="0" y1="0" x2="1" y2="1">
        <stop offset="0" stop-color="#3a1a1e"/>
        <stop offset=".35" stop-color="#4d4f58"/>
        <stop offset=".6" stop-color="#24305a"/>
        <stop offset="1" stop-color="#c9ccd2"/>
      </linearGradient>
      <radialGradient id="enginePhoto" cx=".45" cy=".5" r=".6">
        <stop offset="0" stop-color="#8d8f93"/>
        <stop offset="1" stop-color="#2b2e33"/>
      </radialGradient>
      <radialGradient id="partsGlow" cx=".85" cy=".35" r=".5">
        <stop offset="0" stop-color="#7a0012" stop-opacity=".7"/>
        <stop offset="1" stop-color="#7a0012" stop-opacity="0"/>
      </radialGradient>
    </defs>

    <rect class="red-field" width="2075" height="763" fill="url(#redField)"/>
    <rect width="2075" height="668" fill="url(#partsGlow)" role="img" aria-label="Faint red-toned truck engine parts in the background"/>

    <path class="curve-black" d="M0 0 H725 Q830 330 660 668 H0 Z" fill="var(--ink)"/>
    <path class="curve-white" d="M0 0 H660 Q775 330 640 668 H0 Z" fill="#e6e6e6"/>
    <path class="photo-workshop" d="M0 0 H640 Q752 330 622 668 H0 Z" fill="url(#workshopPhoto)"
          role="img" aria-label="Mechanic in navy overalls and gloves working on a truck engine bay"/>

    <circle cx="686" cy="432" r="132" fill="#e6e6e6"/>
    <circle cx="686" cy="432" r="121" fill="url(#enginePhoto)"
            role="img" aria-label="Hand holding a wrench over an engine"/>

    <rect class="brand-band" y="668" width="2075" height="95" fill="var(--ink)"/>

    <circle class="client-badge" cx="1866" cy="682" r="190" fill="var(--ink)" stroke="var(--white)" stroke-width="6"/>
  </svg>

  <p class="kicker">COMPREHENSIVE MEDIUM AND HEAVY-DUTY REPAIR</p>
  <h1 class="headline">TRUCK AND BUS REPAIRS</h1>
  <p class="tagline">we are equipped to handle even the toughest heavy-duty repair projects.</p>

  <ul class="services">
    <li>Hydraulic Repairs</li>
    <li>Inframe Rebuilds</li>
    <li>Lift Gate Repairs</li>
    <li>ECM Replacements</li>
    <li>Full AC Repairs</li>
    <li>Full Programming</li>
  </ul>

  <div class="contact contact-phones">
    <span class="phone">
      <svg class="icon" viewBox="0 0 16 16" aria-hidden="true"><rect width="16" height="16" rx="3" fill="#d01020"/><path d="M4.5 3.5l2 .2.8 2.3-1.2 1a6 6 0 0 0 2.9 2.9l1-1.2 2.3.8.2 2c-.2.6-.8 1-1.4 1A8.5 8.5 0 0 1 3.5 4.9c0-.6.4-1.2 1-1.4z" fill="var(--ink)"/></svg>
      555-347-0175
    </span>
    <span class="phone">
      <svg class="icon" viewBox="0 0 16 16" aria-hidden="true"><rect width="16" height="16" rx="3" fill="#d01020"/><path d="M4.5 3.5l2 .2.8 2.3-1.2 1a6 6 0 0 0 2.9 2.9l1-1.2 2.3.8.2 2c-.2.6-.8 1-1.4 1A8.5 8.5 0 0 1 3.5 4.9c0-.6.4-1.2 1-1.4z" fill="var(--ink)"/></svg>
      555-329-0160
    </span>
  </div>
  <div class="contact contact-address">
    <svg class="icon" viewBox="0 0 16 16" aria-hidden="true"><path d="M8 0a5.5 5.5 0 0 0-5.5 5.5C2.5 10 8 16 8 16s5.5-6 5.5-10.5A5.5 5.5 0 0 0 8 0zm0 8a2.4 2.4 0 1 1 0-4.8A2.4 2.4 0 0 1 8 8z" fill="var(--ink)"/></svg>
    4120 Harlow Ct #4 Brennan, VA 20190
  </div>

  <ul class="brand-strip" aria-label="Vehicle makes serviced">
    <li>Varn</li><li>Dastorene</li><li>Meridian</li><li>Korvo</li><li>Tarin</li><li>Brin</li>
    <li class="group-gap"></li>
    <li>Skyhauler</li><li>Imura</li><li>Kestrel</li><li>NCL</li><li>Van Dorne</li>
    <li class="group-gap"></li>
    <li>Dovra</li><li>VK</li><li>Pelloway</li><li>Pelterline</li><li>Voltan</li><li>Lakemont</li>
  </ul>

  <div class="client-mark">
    <p class="client-name">RIDGEWAY</p>
    <p class="client-sub">TRUCK &amp; BUS CENTER</p>
  </div>
</section>
</body>
</html>
```